BrambleByte Development Studio Website

We'd like to create a brand new website for our company, so we can display our portfolio, our team, and our general approach to the app development work that we do. We've attached the website content + portfolio images for your convenience.

Our company is focused on substance over glamour, so we want our website to represent that mentality. We need something simple, and clean. We're open to both minimalist designs and as well as bolder designs.

Target Market(s)

Businesses: Startups and established companies

Coding

Coded - Design and coding required

Number of Pages Required

2 page

Font styles to use
Sans Serif

Colors
f78f20
faa54b
ffffff

Requirements
Must have
• We'd like this project to incorporate an orange highlight colour (#FFA300), but otherwise be more or less, black and white. If you'd like to also add a primary colour in your design (outside of the orange and grayscale colours), we're happy to explore it!

NOTICE: At the top of the portfolio section, we'd like a full banner highlighted section for Corvalux (a SaaS platform owned and operated by BrambleByte).
Nice to have
• We want the website design to be more on the clean side, for example, look at the portfolio section from: https://www.lanternandkite.co.uk/ (ignore the top banner).

We're also open to exploring bold designs, something like: https://pelvo.net/

```html
<!DOCTYPE html>
<html lang="en">
<head>
<meta charset="utf-8">
<title>BrambleByte — Digital Products by Experienced Entrepreneurs</title>
<link rel="stylesheet" href="https://fonts.googleapis.com/css2?family=Poppins:wght@400;500;600;700&family=Roboto:wght@400;500;700;900&display=swap">
<style>
:root{
  --orange:#f78f20;
  --orange-deep:#f47b00;
  --orange-soft:#faa54b;
  --peach:#fde3c4;
  --white:#ffffff;
  --ink:#111111;
  --text:#333333;
  --grey-bg:#f6f6f6;
  --footer-bg:#fafafa;
}
*{box-sizing:border-box;margin:0;padding:0}
html,body{width:1200px;height:3909px;overflow:hidden;background:var(--white)}
body{font-family:"Poppins",sans-serif;color:var(--text);position:relative}
.abs{position:absolute}
h1,h2,h3{font-family:"Roboto",sans-serif;font-weight:400;color:var(--ink)}
.btn-pill{display:inline-flex;align-items:center;gap:6px;background:var(--orange);color:var(--white);font:600 11px "Poppins",sans-serif;border-radius:20px;padding:6px 14px;text-transform:uppercase;letter-spacing:.3px}
.btn-pill::after{content:"";width:8px;height:8px;border-radius:50%;background:var(--white)}
.art{border-radius:8px}

/* hero */
.hero{left:0;top:0;width:1200px;height:620px}
.brand{font:700 20px "Poppins",sans-serif;color:var(--ink);display:flex;align-items:center;gap:8px}
.brand .dot{width:14px;height:14px;border-radius:50%;background:var(--orange)}
.nav a{position:absolute;color:var(--white);font:500 13px "Poppins",sans-serif;text-decoration:none;white-space:nowrap}
.nav-cta{left:1054px;top:24px;border:1.5px solid var(--white);border-radius:14px;color:var(--white);font:500 12px "Poppins",sans-serif;padding:3px 14px}
.hero-kicker{left:59px;top:222px;font:500 18px "Roboto",sans-serif;color:var(--ink)}
.hero-title{left:59px;top:252px;font-size:41px;line-height:46px;width:540px}

/* about */
.eyebrow{font:500 15px "Roboto",sans-serif;color:var(--ink)}
.sec-title{font-size:34px;color:var(--ink)}
.about-copy{left:720px;top:750px;width:360px;font-size:15px;line-height:24px;color:var(--ink)}

/* portfolio */
.pf-desc{left:117px;top:1230px;width:420px;font:500 27px/37px "Roboto",sans-serif;color:#444}
.pf-desc b{color:var(--ink);font-weight:700}
.pf-tags{left:117px;top:1384px;font:500 16px "Roboto",sans-serif;color:var(--ink)}
.arrows{display:flex;gap:22px}
.arrows svg{width:34px;height:12px}

/* approach */
.approach-list{left:706px;top:1770px;width:400px;font-size:11px;line-height:16px;color:#555}
.approach-list h4{font:600 13px "Poppins",sans-serif;color:var(--ink);margin-top:10px}
.approach-list h4 span{font-weight:500;font-size:11px}

/* testimonials */
.center{left:0;width:1200px;text-align:center}
.t-card{width:283px;height:285px;padding:28px 30px;text-align:center;font-size:12px;line-height:19px;color:#333}
.t-card.lift{background:var(--white);box-shadow:0 4px 22px rgba(0,0,0,.12)}
.quote{color:var(--orange);font:700 44px/30px "Roboto",sans-serif;text-align:left;height:26px;margin-left:-6px}
.t-name{margin-top:8px;font-size:11px}
.stars{color:var(--orange);letter-spacing:3px;font-size:13px;margin-top:14px}

/* team */
.team-copy{left:634px;top:3096px;width:430px;font-size:15px;line-height:24px;color:#333}
.team-copy h3{font:700 19px "Roboto",sans-serif;margin-bottom:16px}
.team-copy h3 span{font-weight:500;font-size:16px}

/* cta */
.cta{left:0;top:3417px;width:1200px;height:151px;background:var(--orange)}
.cta h2{position:absolute;left:99px;top:38px;color:var(--white);font:500 29px "Roboto",sans-serif}
.cta p{position:absolute;left:99px;top:88px;width:580px;color:var(--white);font-size:13px;line-height:20px}
.cta .btn{position:absolute;left:949px;top:53px;width:156px;height:42px;background:var(--white);border-radius:5px;color:var(--orange);font:600 18px/42px "Roboto",sans-serif;text-align:center}

/* footer */
.footer{left:0;top:3568px;width:1200px;height:303px;background:var(--footer-bg)}
.f-col h5{font:700 16px "Roboto",sans-serif;color:var(--ink);letter-spacing:.4px;margin-bottom:12px}
.f-col li{list-style:none;font:500 11px/21px "Roboto",sans-serif;color:var(--ink)}
.contact li{display:flex;gap:8px;align-items:flex-start;line-height:15px;margin-bottom:8px}
.contact svg{width:10px;height:12px;flex:none;margin-top:2px}
.social{display:flex;gap:14px}
.social span{width:18px;height:18px;border-radius:50%;border:2px solid #333}
.copyright{left:0;top:3871px;width:1200px;height:38px;background:var(--orange-soft);opacity:.55}
.copyright-text{left:0;top:3883px;width:1200px;text-align:center;font-size:10px;color:var(--ink)}
</style>
</head>
<body>

<!-- HERO -->
<section class="abs hero">
  <svg class="abs" style="left:0;top:0" width="1200" height="620" viewBox="0 0 1200 620">
    <defs>
      <linearGradient id="heroOrange" x1="0" y1="0" x2="1" y2="1">
        <stop offset="0" stop-color="#f9a03a"/><stop offset="1" stop-color="#f47b00"/>
      </linearGradient>
    </defs>
    <path d="M520 0 C560 70 680 40 700 120 C720 190 650 250 700 320 C760 420 980 380 1200 470 L1200 0Z" fill="#fde0bd"/>
    <path d="M548 0 C590 60 700 30 725 115 C745 185 680 240 725 305 C780 395 990 360 1200 450 L1200 0Z" fill="url(#heroOrange)"/>
    <path d="M0 540 C200 505 420 505 640 528 C860 552 1020 575 1200 590 L1200 608 C1020 592 850 575 630 556 C410 538 200 540 0 556Z" fill="var(--orange)"/>
  </svg>
  <div class="abs brand" style="left:66px;top:28px"><span class="dot"></span>BrambleByte</div>
  <nav class="abs nav" style="left:0;top:30px">
    <a style="left:610px">Home</a>
    <a style="left:690px">Who We Are</a>
    <a style="left:816px">Portfolio</a>
    <a style="left:917px">Team</a>
  </nav>
  <span class="abs nav-cta">Get Started</span>
  <p class="abs hero-kicker">Digital Products by Experienced Entrepreneurs</p>
  <h1 class="abs hero-title">Where Software Engineering and Business Strategy Collide</h1>
  <span class="abs btn-pill" style="left:59px;top:402px">Read More</span>
  <div class="abs art" role="img" aria-label="Illustration of people working around a large presentation board with charts and a laptop"
       style="left:622px;top:160px;width:540px;height:330px;background:linear-gradient(135deg,#fbd3a3,#f5f5f5 55%,#f68a1c)"></div>
</section>

<!-- WHO WE ARE -->
<section>
  <div class="abs art" role="img" aria-label="Illustration of a briefcase, brain, light bulb and two people celebrating with a trophy"
       style="left:103px;top:663px;width:516px;height:293px;background:linear-gradient(135deg,#fcd7a8,#f7a64a 60%,#3d4a5c);border-radius:40% 46% 40% 38%"></div>
  <p class="abs eyebrow" style="left:720px;top:667px">About Us</p>
  <h2 class="abs sec-title" style="left:720px;top:690px">Who We Are</h2>
  <p class="abs about-copy">Non-technical entrepreneurs who aspire to bring their ideas to life Businesses looking to implement strategic tech solutions Larger enterprises looking to roll out new initiatives ideas to life Businesses looking to implement strategic tech solutions Larger enterprises looking to roll out new initiatives</p>
</section>

<!-- PORTFOLIO -->
<section>
  <p class="abs eyebrow" style="left:117px;top:1152px">Our Work</p>
  <h2 class="abs sec-title" style="left:117px;top:1174px">Portfolio</h2>
  <p class="abs pf-desc"><b>Description:</b> Secondary Marketplace Solution For Stone Fabricators And Design Professionals</p>
  <p class="abs pf-tags">Design, Consulting, Web App, Mobile App</p>
  <span class="abs btn-pill" style="left:117px;top:1428px">Show More</span>
  <svg class="abs" style="left:780px;top:1120px" width="420" height="420" viewBox="0 0 420 420">
    <path d="M140 40 C220 -10 380 10 420 60 L420 400 C300 430 160 400 90 330 C20 260 60 90 140 40Z" fill="var(--peach)"/>
  </svg>
  <p class="abs" style="left:962px;top:1296px;font:900 36px 'Roboto',sans-serif;color:var(--ink)">Slabmarket</p>
  <div class="abs" role="img" aria-label="Screenshot of the marketplace web app showing a product list and listing detail panel"
       style="left:579px;top:1168px;width:378px;height:300px;background:linear-gradient(180deg,#ffffff,#eef0f3);box-shadow:0 4px 18px rgba(0,0,0,.18);border-top:24px solid #f3f3f3"></div>
  <div class="abs arrows" style="left:1010px;top:1506px">
    <svg viewBox="0 0 34 12"><path d="M34 6H3M8 1L2 6L8 11" stroke="var(--orange)" stroke-width="2" fill="none"/></svg>
    <svg viewBox="0 0 34 12"><path d="M0 6H31M26 1L32 6L26 11" stroke="var(--orange)" stroke-width="2" fill="none"/></svg>
  </div>
</section>

<!-- OUR APPROACH -->
<section>
  <svg class="abs" style="left:0;top:1575px" width="1200" height="700" viewBox="0 0 1200 700">
    <path d="M0 90 C200 10 420 -10 650 40 C850 80 1000 40 1200 60 L1200 610 C1000 680 800 560 600 600 C400 640 200 700 0 640Z" fill="var(--grey-bg)"/>
  </svg>
  <h2 class="abs center" style="top:1668px;font-size:29px">Our Approach</h2>
  <div class="abs art" role="img" aria-label="Illustration of a developer working at a laptop beside a window with coding language tags"
       style="left:99px;top:1761px;width:506px;height:398px;background:linear-gradient(135deg,#fde3c4,#f9b86a 55%,#3b3f4a)"></div>
  <div class="abs approach-list">
    <h4>Focus ; <span>We only play within our realm of excellence</span></h4>
    <p>Our focus is helping you design, launch and evolve your mobile / web technology solutions.</p>
    <h4>Quality over Quantity ; <span>We engage more deeply in fewer projects</span></h4>
    <p>Our trusted core team is only focused on a handful of projects and we typically work with our clients on an on-going basis to refine and evolve their offering in the market.</p>
    <h4>Entrepreneurial at Heart ; <span>Operating with a scrappy and multi-disciplinary approach</span></h4>
    <p>We've learned to do more with less, so we can provide top-notch value for your dollar. When working with us, you work directly with the owner-operators and their core team of local experts.</p>
    <h4>Function over Flash ; <span>Simple, effective execution takes priority over glamour</span></h4>
    <p>Our primary interest is in helping you maximize your key business metrics through technical excellence, sound strategy, and a keen understanding of your end-user.</p>
  </div>
</section>

<!-- TESTIMONIALS -->
<section>
  <h2 class="abs center" style="top:2318px;font-size:30px">Our Testimonial</h2>
  <p class="abs center" style="top:2374px;font-size:14px;color:#333">Let's get testimonials from everyone (except SS obviously)</p>
  <article class="abs t-card" style="left:120px;top:2440px">
    <div class="quote">&ldquo;</div>
    <p>Lorem ipsum dolor sit amet, consetetur sadipscing elitr, sed diam nonumy eirmod tempor invidunt ut labore et dolore magna aliquyam erat, sed diam voluptua. At vero eos et accusam et justo duo dolores et ea rebum. Stet clita kasd gubergren, no sea takimata sanctus est Lorem ipsum dolor sit</p>
    <p class="t-name">Mara Quill</p><p class="stars">★★★★★</p>
  </article>
  <article class="abs t-card lift" style="left:463px;top:2440px">
    <div class="quote">&ldquo;</div>
    <p>Lorem ipsum dolor sit amet, consetetur sadipscing elitr, sed diam nonumy eirmod tempor invidunt ut labore et dolore magna aliquyam erat, sed diam voluptua. At vero eos et accusam et justo duo dolores et ea rebum. Stet clita kasd gubergren, no sea takimata sanctus est Lorem ipsum dolor sit</p>
    <p class="t-name">Owen Pike</p><p class="stars">★★★★★</p>
  </article>
  <article class="abs t-card" style="left:797px;top:2440px">
    <div class="quote">&ldquo;</div>
    <p>Lorem ipsum dolor sit amet, consetetur sadipscing elitr, sed diam nonumy eirmod tempor invidunt ut labore et dolore magna aliquyam erat, sed diam voluptua. At vero eos et accusam et justo duo dolores et ea rebum. Stet clita kasd gubergren, no sea takimata sanctus est Lorem ipsum dolor sit</p>
    <p class="t-name">Lena Frost</p><p class="stars">★★★★★</p>
  </article>
  <div class="abs arrows" style="left:1010px;top:2768px">
    <svg viewBox="0 0 34 12"><path d="M34 6H3M8 1L2 6L8 11" stroke="var(--orange)" stroke-width="2" fill="none"/></svg>
    <svg viewBox="0 0 34 12"><path d="M0 6H31M26 1L32 6L26 11" stroke="var(--orange)" stroke-width="2" fill="none"/></svg>
  </div>
</section>

<!-- EXECUTIVE TEAM -->
<section>
  <h2 class="abs center" style="top:2946px;font-size:30px">Executive Team</h2>
  <p class="abs center" style="top:2990px;font-size:13px;line-height:21px;color:#333">Lorem ipsum dolor sit amet, consetetur sadipscing elitr, sed diam nonumy eirmod<br>tempor invidunt ut labore et dolore magna aliquyam erat, sed diam voluptua. At vero eos et accusam et justo duo</p>
  <div class="abs" role="img" aria-label="Portrait photograph of the cofounder in a dark suit in an office"
       style="left:174px;top:3076px;width:381px;height:231px;border-radius:12px;background:linear-gradient(135deg,#6b4a36,#2d2a2a 60%,#8a6a52)"></div>
  <div class="abs team-copy">
    <h3>Cofounder ; <span>Idris Calloway, Cofounder</span></h3>
    <p>Idris is an Engineer, full-stack developer and award-winning entrepreneur. He was recognized and awarded by Sir Alden Marsh for his earlier entrepreneurial work. He is also the founder and technology lead for Corvalux, a SaaS solution recognized by the construction industry throughout North America.</p>
  </div>
  <div class="abs arrows" style="left:1010px;top:3341px">
    <svg viewBox="0 0 34 12"><path d="M34 6H3M8 1L2 6L8 11" stroke="var(--orange)" stroke-width="2" fill="none"/></svg>
    <svg viewBox="0 0 34 12"><path d="M0 6H31M26 1L32 6L26 11" stroke="var(--orange)" stroke-width="2" fill="none"/></svg>
  </div>
</section>

<!-- CTA -->
<section class="abs cta">
  <h2>Start Your 14 Day Free Trial</h2>
  <p>Lorem ipsum dolor sit amet, consetetur sadipscing elitr, sed diam nonumy eirmod tempor invidunt ut labore et dolore magna aliquyam erat, sed</p>
  <span class="btn">Get Started</span>
</section>

<!-- FOOTER -->
<footer class="abs footer">
  <div class="abs" role="img" aria-label="Faint grey corner decoration" style="left:0;top:0;width:110px;height:150px;background:linear-gradient(135deg,#e6e6e6,rgba(230,230,230,0))"></div>
  <div class="abs" role="img" aria-label="Faint orange corner decoration" style="left:1090px;top:190px;width:110px;height:113px;background:linear-gradient(315deg,#fde3c4,rgba(253,227,196,0))"></div>
  <div class="abs brand" style="left:150px;top:110px;font-size:22px"><span class="dot"></span>BrambleByte</div>
  <p class="abs" style="left:131px;top:144px;width:250px;font-size:11px;line-height:15px;color:#333">Lorem ipsum dolor sit amet, consetetur sadipscing elitr, sed diam nonumy eirmod tempor invidunt ut labore et</p>
  <div class="abs f-col" style="left:466px;top:96px">
    <h5>USEFULL LINKS</h5>
    <ul><li>HOME</li><li>Who We Are</li><li>Team</li><li>Testimonial</li><li>Portfolio</li><li>Approuch</li></ul>
  </div>
  <div class="abs f-col contact" style="left:686px;top:96px">
    <h5>CONTACT US</h5>
    <ul>
      <li><svg viewBox="0 0 10 12"><path d="M5 0C2.2 0 0 2.1 0 4.8 0 8 5 12 5 12S10 8 10 4.8C10 2.1 7.8 0 5 0Z" fill="#222"/><circle cx="5" cy="4.8" r="1.8" fill="#fff"/></svg><span>48 Harbor Lane, New<br>York, NY 10031</span></li>
      <li><svg viewBox="0 0 10 12"><path d="M2 1L4 1 5 4 3.5 5C4 6.5 5 7.5 6.5 8L7.5 6.5 10 7.5 10 10C6 11 0 6 2 1Z" fill="#222"/></svg><span>+44(0)20 4000-1234</span></li>
      <li><svg viewBox="0 0 10 12"><rect x="0" y="3" width="10" height="7" fill="#222"/><path d="M0 3L5 7 10 3" stroke="#fff" fill="none"/></svg><span>info@brambleworks.com</span></li>
    </ul>
  </div>
  <div class="abs f-col" style="left:929px;top:96px">
    <h5>SOCIAL LINKS</h5>
    <div class="social" style="margin-left:14px"><span></span><span></span><span></span></div>
  </div>
</footer>
<div class="abs copyright"></div>
<p class="abs copyright-text">© 2021 brambleworks.com. All Rights</p>

</body>
</html>
```